Plastic Surgeon Needs a business card desing

I need a plastic surgeon business card, Im young , innovative , not afraid of thinking out of the box, What I dont like is human figures or scalpes as designing the card, because I think they are old fashion, I think my name is my strongest card, so I try to find the desing to be something elegant , simple , slick , stylish , radiant with carimsa!

Target Market(s)

PLastics Surgery Patients and doctors to have my data

Industry/Entity Type

Plastic

Contact Information for Business Card

phone numbers need to be legible , right now i have grey scales so they a not to legible

Font styles to use
Serif
Sans Serif

Requirements
Must have
• Personality, and it has to look like a doctor card, not a buisness man card, that is why i think it should be clean , clear , and legible
Nice to have
• Stylilsh, not to heavy card, in means of colors and logos, i think it should give a sensation of health
• Im not sure to have the logo of the hospital i work
Should not have
• human figures
• Hands
• Surgeons

```html
<!DOCTYPE html>
<html lang="es">
<head>
<meta charset="utf-8">
<title>Dr. Andrés Velmar — Tarjeta de presentación</title>
<link href="https://fonts.googleapis.com/css2?family=Mulish:wght@400;700&display=swap" rel="stylesheet">
<style>
  :root {
    --backdrop: #4b4b4d;
    --card: #bfbfbf;
    --card-edge: #b3b3b3;
    --ink: #ffffff;
    --ink-soft: #f4f4f4;
  }
  * { box-sizing: border-box; margin: 0; padding: 0; }
  html, body {
    width: 1200px;
    height: 864px;
    overflow: hidden;
    background: var(--backdrop);
    font-family: "Mulish", "Helvetica Neue", Arial, sans-serif;
  }
  .sheet {
    width: 1200px;
    height: 864px;
    display: flex;
    align-items: center;
    justify-content: center;
    gap: 64px;
  }
  .card {
    background: var(--card);
    box-shadow: 0 0 0 1px var(--card-edge), 0 18px 40px rgba(0, 0, 0, 0.35);
    color: var(--ink);
    position: relative;
  }
  .card--front {
    width: 560px;
    height: 320px;
    padding: 52px 48px;
    display: flex;
    flex-direction: column;
    justify-content: center;
  }
  .card--back {
    width: 320px;
    height: 560px;
    display: flex;
    align-items: center;
    justify-content: center;
    gap: 12px;
  }
  .doctor-name {
    font-weight: 700;
    font-size: 24px;
    letter-spacing: 0.08em;
    text-transform: uppercase;
  }
  .specialty {
    font-size: 13px;
    letter-spacing: 0.04em;
    margin-top: 4px;
    color: var(--ink-soft);
  }
  .contact {
    margin-top: 30px;
    font-size: 15px;
    line-height: 1.45;
    font-style: normal;
  }
  .contact__block + .contact__block { margin-top: 12px; }
  .brand-mark {
    width: 12px;
    height: 12px;
    border-radius: 50%;
    background: var(--ink);
  }
  .brand-name {
    font-weight: 700;
    font-size: 20px;
    letter-spacing: 0.06em;
    text-transform: uppercase;
    color: var(--ink);
  }
</style>
</head>
<body>
  <main class="sheet">
    <section class="card card--front" aria-label="Frente de la tarjeta">
      <h1 class="doctor-name">Dr. Andrés Velmar</h1>
      <p class="specialty">Cirugía Plástica</p>
      <address class="contact">
        <div class="contact__block">
          Av. Lirios 2150 Int 304<br>
          Torre Médica Aurora<br>
          Zapopan, Jal. México
        </div>
        <div class="contact__block">
          Tel. 01 (33) 3555 0142<br>
          Cel. 33 3555 0187<br>
          andres@drvelmar.com<br>
          www.drvelmar.com
        </div>
      </address>
    </section>

    <section class="card card--back" aria-label="Reverso de la tarjeta">
      <span class="brand-mark" aria-hidden="true"></span>
      <span class="brand-name">Velmar</span>
    </section>
  </main>
</body>
</html>
```